A4 double sided brochure for progressive, young lawyers

Hi designers, we would like a double sided A4 flyer advertising:

Designers, Side 1 flyer contents:

Main heading #1 on side 1: Wills

A comprehensive, legal Will gives you peace of mind.

It ensures that your wealth is distributed according to your wishes.

As your life changes, so should your Will. It should reflect evolving circumstances, such as:
- separation or divorce
- assets disposed of or acquired
- the birth or death of beneficiaries
- minor beneficiaries coming of age
- the death or incapacity of an executor

Our lawyers will listen to your wishes and provide tailored advice to suit your needs.

Main heading #2 on side 1 : Testamentary Discretionary Trusts

Did you know that your beneficiaries may have to pay tax on property you leave them in your Will? You can better protect them and minimise potential tax by income streaming with testamentary discretionary trusts.

(Note to Designers: I have attached a word document containing information that I would like to appear under this sentence which includes a few paragraphs and a data table. Please include all information from the word document here in a similar kind or format.)

(Our Call to Action): K.T. Marlow Lawyers has a team of experienced lawyers who can advise you on drafting an effective Will.

Call or email one of our friendly Principals, Rohan Marlow or Priya Marlow for a quick, no-obligation quote.

Designers, side 2 flyer content is as follows:

Main heading side 2: Planning Ahead

Estate Planning is not just about having a Will.

It involves your personal, family and business matters, both now and after you pass away.

While it may be as simple as having a Will, it most cases it also involves having Powers of Attorney, Enduring Guardianships and Advance Health Care planning.

Estate planning is about planning ahead for your current lifestyle needs, you retirement plans, your business arrangements, your tax and superannuation position, future events (like divorce, ill-health and family disputes) and ultimately, ensuring your assets go exactly where you want them to.

Simply put, it gives you peace of mind.

Heading #2 on side 2: What else should I consider now?

[Designers, I am happy for you to put the below 3 points into a picture diagram or some kind of list format - whatever looks less boring!

1. A Power of Attorney - This enables you to appoint a trusted person to act on your behalf if you are unable to, or simply don’t wish to, make decisions about your financial and legal affairs.

[DESIGNERS - please highlight, enlarge or emphasize the words 'power of attorney']

2. A Power of Enduring Guardianship - This enables you to appoint a trusted person to act on your behalf if you are unable (through mental incapacity) to make decisions about your health and welfare issues.

[DESIGNERS - please somehow highlight the words 'power of enduring guardianship']

3. An Advance Health Care Plan - This directs your doctors, medical staff and family how you wish to be treated. Remember, you have the right to accept or refuse medical treatment.

[DESIGNERS - please highlight the words 'Advance Health Care Plan']

(Our Call to Action):

K.T. Marlow Lawyers has a team of experienced lawyers who can advise you on preparing a Will, Powers of Attorney and Powers of Enduring Guardianship, estate planning and administration of a deceased estate.

Industry/Entity Type

Legal

Font styles to use
Sans Serif

Requirements
Must have
• Colours should match our logo. See our website www.ktmarlow.com.au also for colours. Please not too much red blocks areas though.
• Our firm name is: K.T. Marlow Lawyers
• Note to designers - Both sides should have contact details of our 2 offices and other contact information including:
• For more information contact our Principals:
• Rohan Marlow or Priya Marlow
• Office locations:
• BEXLEY NORTH:
• Shop 5, 14-32 Dunmore Crescent,
• Bexley North NSW 2207
• Phone: (02) 9384 2175
• ENGADINE:
• 7 Kestrel Lane,
• Engadine NSW
• Phone: (02) 9673 4809
• Email: admin@ktmarlow.com.au
• Web: www.ktmarlow.come.au
• Connect with us on Facebook:
• www.facebook.com/ktmarlowlawyers
• Must have 2 pages (back and front of flyer). See project description for details.
• I would like all information contained in the project description and all information contained in my word doc attached to be included in the brochure. Please do not edit the words or the structure of the information.
• The data table (in the word doc attached) must be replicated exactly as it appears including the fine print.
Should not have
• Too many block red areas or too much red.
• I want it to be eye catching but not too bright to read.

```html
<!DOCTYPE html>
<html lang="en">
<head>
<meta charset="utf-8">
<title>K.T. Marlow Lawyers – Estate Planning Flyer</title>
<link rel="stylesheet" href="https://fonts.googleapis.com/css2?family=Lobster&family=Montserrat:wght@600;700;800&family=Lato:wght@400;700;900&display=swap">
<style>
:root{
  --bg:#e4e4e4;
  --slate:#3b4858;
  --slate-dark:#2e3a48;
  --teal:#8fd2de;
  --red:#b7202c;
  --maroon:#7a3342;
  --wood:#c7bab1;
  --wood-dark:#b5a79d;
  --shelf:#8b6b56;
  --text:#3a3535;
  --tick:#7dc04b;
  --row1:#5f7189;
  --row2:#8193aa;
}
*{box-sizing:border-box;margin:0;padding:0}
html,body{width:1200px;height:1000px;overflow:hidden}
body{background:var(--bg);font-family:"Lato",sans-serif;position:relative}
.page{position:absolute;top:140px;width:508px;height:720px;overflow:hidden;background:linear-gradient(180deg,var(--wood),var(--wood-dark));box-shadow:0 2px 8px rgba(0,0,0,.25)}
.page--front{left:55px}
.page--back{left:630px}
.abs{position:absolute}
.hero{position:absolute;left:0;top:0;width:100%;background:linear-gradient(160deg,#475668,var(--slate-dark))}
.shelf{position:absolute;left:0;width:100%;height:18px;background:linear-gradient(180deg,#a07e66,var(--shelf) 60%,#5d4536)}
.script{font-family:"Lobster",sans-serif;color:var(--red);position:absolute;line-height:1}
.photo{position:absolute;border-radius:4px}
.title{font-family:"Montserrat",sans-serif;font-weight:700;color:var(--teal);font-size:18px;line-height:22px;letter-spacing:-0.2px;text-transform:uppercase;white-space:nowrap}
.white{color:#fff}
.red-line{color:var(--red);font-family:"Montserrat",sans-serif;font-weight:700;text-transform:uppercase}
.rule{position:absolute;height:1px;background:rgba(255,255,255,.45)}
.ticks{list-style:none}
.ticks li{position:relative;padding-left:16px}
.ticks li::before{content:"✓";position:absolute;left:0;color:var(--tick);font-weight:900}
.section-head{position:absolute;left:0;font-family:"Montserrat",sans-serif;font-weight:700;font-size:16px;color:var(--maroon);padding-left:18px}
.section-head::before{content:"";position:absolute;left:0;top:3px;width:12px;height:14px;background:var(--maroon)}
.body-copy{font-size:9.5px;line-height:12.4px;color:var(--text)}
.sub-head{font-family:"Montserrat",sans-serif;font-weight:700;font-size:10.5px;color:var(--maroon)}
.step-box{position:absolute;background:var(--maroon);color:#fff;font-size:5.8px;line-height:7.2px;text-align:center;border:1px solid #e6cfd4;border-radius:2px;display:flex;align-items:center;justify-content:center;padding:2px 3px;overflow:hidden}
.tax-badge{position:absolute;border:3px solid var(--maroon);border-radius:12px;text-align:center;color:var(--maroon);font-family:"Montserrat",sans-serif;font-weight:800;background:rgba(255,255,255,.12)}
.rates{position:absolute;border-collapse:collapse;font-size:7.5px;color:#fff;text-align:center}
.rates th{background:var(--slate);font-weight:700;height:15px}
.rates td{height:15px}
.rates tr:nth-child(odd) td{background:var(--row1)}
.rates tr:nth-child(even) td{background:var(--row2)}
.footer{position:absolute;left:0;top:663px;width:100%;height:39px;background:#fff;border-top:2px solid var(--maroon)}
.brand{position:absolute;left:10px;top:7px;font-family:"Lato",sans-serif;font-weight:900;font-size:13px;color:var(--maroon);letter-spacing:.5px;line-height:1}
.brand-sub{display:block;font-size:8px;letter-spacing:2px;margin-top:3px}
.contact{position:absolute;left:140px;top:4px;font-size:6.8px;line-height:10px;color:#333;white-space:nowrap}
.contact b{font-weight:900}
.contact .phone{color:var(--red);font-weight:900;font-size:8px}
.links{position:absolute;left:0;top:702px;width:100%;height:18px;background:linear-gradient(180deg,#b9aca3,#a5978d);font-size:8px;font-weight:700;letter-spacing:.5px;color:var(--slate-dark);text-align:center;line-height:18px;word-spacing:2px}
.number{position:absolute;font-family:"Montserrat",sans-serif;font-weight:800;font-size:46px;color:var(--teal);line-height:1}
.item-title{font-family:"Montserrat",sans-serif;font-weight:700;font-size:10.5px;color:var(--teal);text-transform:uppercase}
.item-copy{font-size:9px;line-height:11px;color:#fff;font-weight:700}
.caps-list{list-style:none;font-family:"Montserrat",sans-serif;font-weight:600;font-size:10.5px;line-height:15.5px;color:var(--slate-dark);text-transform:uppercase}
.caps-list li{position:relative;padding-left:16px}
.caps-list li::before{content:"✓";position:absolute;left:0;color:var(--maroon);font-weight:900}
</style>
</head>
<body>

<!-- FRONT -->
<section class="page page--front">
  <div class="hero" style="height:255px"></div>
  <div class="script" style="left:18px;top:22px;font-size:56px">Wills</div>
  <h1 class="abs title" style="left:165px;top:19px">A comprehensive, legal Will<br>gives you peace of mind.</h1>
  <p class="abs white" style="left:165px;top:66px;font-size:10.5px;font-weight:700">It ensures that your wealth is distributed according to your wishes.</p>
  <div class="rule" style="left:165px;top:84px;width:325px"></div>
  <div class="abs" style="left:165px;top:90px;width:325px;text-align:center">
    <p class="red-line" style="font-size:10px">As your life changes, so should your Will.</p>
    <p class="white" style="font-size:10px;font-weight:700;margin-top:1px">It should reflect evolving circumstances, such as:</p>
  </div>
  <ul class="ticks abs white" style="left:210px;top:119px;font-size:10px;font-weight:700;line-height:17px">
    <li>Separation or divorce</li>
    <li>Assets disposed of or acquired</li>
    <li>The birth or death of beneficiaries</li>
    <li>Minor beneficiaries coming of age</li>
    <li>The death or incapacity of an executor</li>
  </ul>
  <div class="rule" style="left:195px;top:209px;width:265px"></div>
  <p class="abs" style="left:175px;top:214px;width:305px;text-align:center;color:var(--teal);font-size:11px;font-weight:900;line-height:14px">Our lawyers will listen to your wishes and provide tailored advice to suit your needs.</p>
  <div class="photo" role="img" aria-label="Young boy in a red suit and bow tie standing behind an open book" style="left:55px;top:92px;width:110px;height:160px;background:linear-gradient(180deg,#4a5868,#6d2a34 55%,#8a3a44)"></div>
  <div class="photo" role="img" aria-label="Stack of old books at the edge of the shelf" style="left:0;top:125px;width:34px;height:128px;background:linear-gradient(90deg,#8a6d50,#b39572)"></div>
  <div class="shelf" style="top:245px"></div>

  <h2 class="section-head" style="top:278px">Testamentary Discretionary Trusts</h2>
  <p class="abs body-copy" style="left:18px;top:299px;width:475px">Did you know that your beneficiaries may have to pay tax on property you leave them in your Will? You can better protect them and minimise potential tax by income streaming with testamentary discretionary trusts.</p>
  <h3 class="abs sub-head" style="left:18px;top:325px">Income streaming with testamentary discretionary trusts</h3>
  <p class="abs body-copy" style="left:18px;top:340px;width:475px">When a beneficiary in your Will earns income from a gift – eg. rent on an investment property, or capital gains when they sell it – that income will be taxable. While they have children under 18 years old, that income can be ‘streamed’ to the kids to take advantage of their preferential tax rates. This requires a special structure called a ‘testamentary discretionary trust’ that can only be created under a Will.</p>
  <p class="abs sub-head" style="left:18px;top:391px;font-size:9.5px;color:var(--red)">Example:</p>
  <p class="abs body-copy" style="left:18px;top:403px">Mary earns $180K salary and has 4 kids under 18 years old</p>

  <svg class="abs" style="left:24px;top:420px" width="352" height="112" viewBox="0 0 352 112" aria-hidden="true">
    <polygon points="0,34 260,34 260,0 352,56 260,112 260,78 0,78" fill="var(--slate)"/>
  </svg>
  <div class="step-box" style="left:40px;top:442px;width:70px;height:48px">Jane leaves an investment property worth $1M to her daughter Mary.</div>
  <div class="step-box" style="left:118px;top:442px;width:66px;height:48px">Five years later, Mary sells the property for $1.3M, making a $300K capital gain.</div>
  <div class="step-box" style="left:192px;top:428px;width:110px;height:80px;flex-direction:column;line-height:8.5px"><u>Using a ‘simple’ Will</u>Tax = 47% x $300K = $141K<br><br><u>Using a Testamentary Trust</u>($75K streamed to each child)<br>Tax =$15,922 x 4 = $63,688</div>
  <div class="tax-badge" style="left:382px;top:420px;width:100px;height:92px">
    <div style="font-size:25px;line-height:24px;margin-top:6px">TAX</div>
    <div style="font-size:18px;line-height:18px">SAVED</div>
    <div style="font-family:'Lato',sans-serif;font-size:5.5px;font-weight:700">with a testamentary trust</div>
    <div style="font-size:19px;line-height:24px;border-top:2px solid var(--maroon);margin:2px 4px 0">$77,312</div>
  </div>

  <p class="abs" style="left:98px;top:523px;font-size:8.5px;font-weight:900;color:var(--slate-dark)">Income tax rates for resident minors</p>
  <table class="rates" style="left:98px;top:536px;width:303px">
    <tr><th style="width:30%">Distribution ($)</th><th style="width:35%">Family Trust</th><th>Testamentary Trust</th></tr>
    <tr><td>0 – 416</td><td>-</td><td>-</td></tr>
    <tr><td>417 – 1,307</td><td>66%*</td><td></td></tr>
    <tr><td>1,308 – 18,200</td><td>47%*</td><td>-</td></tr>
    <tr><td>18,201 – 37,000</td><td>47%*</td><td>19%</td></tr>
    <tr><td>37,001 – 80,000</td><td>47%*</td><td>32.5%</td></tr>
    <tr><td>80,001 – 180,000</td><td>47%*</td><td>37%</td></tr>
  </table>
  <div class="abs" style="left:316px;top:576px;width:46px;height:68px;border:2px solid var(--maroon);border-radius:7px"></div>

  <div class="footer">
    <div class="brand">K.T. Marlow<span class="brand-sub">LAWYERS</span></div>
    <div class="contact">
      Contact our friendly and experienced Principals, Rohan Marlow and Priya Marlow for a <b>FREE quote</b><br>
      <b>Offices located at:</b>&nbsp; Shop 5, 14-32 Dunmore Crescent | Bexley North NSW 2207 &nbsp;&nbsp; 7 Kestrel Lane | Engadine NSW 2233<br>
      <span style="margin-left:66px" class="phone">Ph (02) 9384 2175</span><span style="margin-left:112px" class="phone">Ph (02) 9673 4809</span>
    </div>
  </div>
  <div class="links">admin@ktmarlow.com.au &nbsp; | &nbsp; www.ktmarlow.com.au &nbsp; | &nbsp; www.facebook.com/ktmarlowlawyers</div>
</section>

<!-- BACK -->
<section class="page page--back">
  <div class="hero" style="height:435px"></div>
  <div class="script" style="left:0;top:22px;width:100%;text-align:center;font-size:58px">Planning Ahead</div>
  <p class="abs" style="left:0;top:104px;width:100%;text-align:center;font-family:'Montserrat',sans-serif;font-weight:700;font-size:11px;color:var(--teal)">ESTATE PLANNING IS NOT JUST ABOUT HAVING A WILL.</p>
  <p class="abs white" style="left:20px;top:124px;width:468px;font-size:9.8px;line-height:12.5px;font-weight:700;text-align:justify">Estate planning is about planning ahead for your current lifestyle needs, you retirement plans, your business arrangements, your tax and superannuation position, future events (like divorce, ill-health and family disputes) and ultimately, ensuring your assets go exactly where you want them to.</p>
  <p class="abs red-line" style="left:176px;top:176px;font-size:12px">Simply put, it gives you peace of mind.</p>
  <div class="photo" role="img" aria-label="Toddler in glasses, blue bow tie and braces leaning on the shelf" style="left:10px;top:190px;width:165px;height:245px;background:linear-gradient(180deg,#4b5a6b,#2b2f3f 50%,#8aa2bf)"></div>
  <p class="abs white" style="left:178px;top:205px;font-family:'Montserrat',sans-serif;font-weight:700;font-size:12.5px">WHAT ELSE SHOULD I CONSIDER NOW?</p>

  <div class="number" style="left:180px;top:225px">1</div>
  <div class="abs" style="left:212px;top:228px;width:282px">
    <p class="item-title">A Power of Attorney</p>
    <p class="item-copy">This enables you to appoint a trusted person to act on your behalf if you are unable to, or simply don’t wish to, make decisions about your financial and legal affairs.</p>
  </div>
  <div class="number" style="left:180px;top:297px">2</div>
  <div class="abs" style="left:212px;top:299px;width:282px">
    <p class="item-title">A Power of Enduring Guardianship</p>
    <p class="item-copy">This enables you to appoint a trusted person to act on your behalf if you are unable (through mental incapacity) to make decisions about your health and welfare issues.</p>
  </div>
  <div class="number" style="left:180px;top:370px">3</div>
  <div class="abs" style="left:212px;top:372px;width:282px">
    <p class="item-title">An Advance Health Care Plan</p>
    <p class="item-copy">This directs your doctors, medical staff and family how you wish to be treated. Remember, you have the right to accept or refuse medical</p>
  </div>
  <div class="shelf" style="top:432px"></div>

  <div class="script" style="left:0;top:462px;width:100%;text-align:center;font-size:32px">Probate &amp; Deceased Estates</div>
  <h2 class="section-head" style="top:512px">Are you an Executor in a Will?</h2>
  <p class="abs body-copy" style="left:22px;top:534px;width:468px;font-size:9.8px;line-height:12.8px;text-align:justify">If you are the Executor named in a Will of someone who recently died, then we can help. Otherwise, if you are the next of kin of a person who died without a Will, it is possible that you may apply to finalise the deceased’s estate. <b style="color:var(--red)">WE CAN:</b></p>
  <ul class="caps-list abs" style="left:95px;top:577px">
    <li>Advise you on your rights and duties</li>
    <li>Obtain grants of probate</li>
    <li>Call in assets and pay debts</li>
    <li>Transfer assets and distribute the estate to beneficiaries</li>
    <li>Deal with disputes</li>
  </ul>

  <div class="footer">
    <div class="brand">K.T. Marlow<span class="brand-sub">LAWYERS</span></div>
    <div class="contact">
      Contact our friendly and experienced Principals, Rohan Marlow and Priya Marlow for a <b>FREE quote</b><br>
      <b>Offices located at:</b>&nbsp; Shop 5, 14-32 Dunmore Crescent | Bexley North NSW 2207 &nbsp;&nbsp; 7 Kestrel Lane | Engadine NSW 2233<br>
      <span style="margin-left:66px" class="phone">Ph (02) 9384 2175</span><span style="margin-left:112px" class="phone">Ph (02) 9673 4809</span>
    </div>
  </div>
  <div class="links">admin@ktmarlow.com.au &nbsp; | &nbsp; www.ktmarlow.com.au &nbsp; | &nbsp; www.facebook.com/ktmarlowlawyers</div>
</section>

</body>
</html>
```